Drink Coaster Design

We will be providing reusable drink coaster for sports bars. The coasters are 4" by 4" with rounded corners. You can see the coasters at this link:
https://www.trayvillemart.example/4-white-square-80-pt-customizable-paper-coaster-case/712KPLM6T93.html. We want the coasters to be impressive and lead customers to our web site and our twitter account.
I have included one design created for us but it does not look impressive. We provide information to sports bettors who use our service to decide which games to bet on in college and professional football and basketball. You can see our web site at www.zenithwageranalytics.example. You can see our twitter account at https://twitter.com/zenithforecast. I have attached several different logos. The goal is to drive traffic to our web site and our twitter account. The design needs to be a conversation "starter" and needs to be impressive. Please visit our web site to understand what we do and to see our key selling points

```html
<!DOCTYPE html>
<html lang="en">
<head>
<meta charset="utf-8">
<title>Zenith Wager Analytics – Drink Coaster</title>
<link rel="stylesheet" href="https://fonts.googleapis.com/css2?family=Roboto+Condensed:ital,wght@0,400;0,700;0,800;1,400&display=swap">
<style>
  :root {
    --ink: #1c1c1c;
    --red: #c0202e;
    --green: #4cb74f;
    --brand-green: #2ee03a;
    --paper: #ffffff;
    --page: #ffffff;
  }
  * { box-sizing: border-box; margin: 0; padding: 0; }
  html, body {
    width: 1200px; height: 1200px; overflow: hidden;
    background: var(--page);
    font-family: "Roboto Condensed", "Arial Narrow", sans-serif;
  }
  .coaster {
    position: absolute; left: 100px; top: 100px;
    width: 1000px; height: 1000px;
    background: var(--paper);
    border: 5px solid var(--ink);
    border-radius: 70px;
    overflow: hidden;
    text-align: center;
  }
  .headline { font-weight: 800; text-transform: uppercase; line-height: 1; }
  .headline__top {
    position: absolute; left: 0; right: 0; top: 26px;
    font-size: 100px; color: var(--ink); letter-spacing: 1px;
  }
  .headline__bottom {
    position: absolute; left: 0; right: 0; top: 122px;
    font-size: 134px; color: var(--red); letter-spacing: 1px;
  }
  .features {
    position: absolute; left: 0; right: 0; top: 282px;
    display: flex; justify-content: space-between; padding: 0 52px;
  }
  .feature { width: 290px; display: flex; flex-direction: column; align-items: center; }
  .feature__icon { width: 200px; height: 200px; }
  .feature__label {
    margin-top: 16px; font-weight: 700; font-size: 36px; line-height: 1.05;
    text-transform: uppercase; color: var(--ink);
  }
  .feature__label em { display: block; font-style: normal; color: var(--red); }
  .prompt {
    position: absolute; left: 0; right: 0; top: 588px;
    font-weight: 800; font-size: 96px; line-height: 1; color: var(--ink);
  }
  .contact-band {
    position: absolute; left: 0; right: 0; top: 693px; height: 150px;
    background: var(--red); color: var(--paper);
    display: flex; flex-direction: column; justify-content: center;
    font-weight: 700; font-size: 46px; line-height: 1.2;
  }
  .contact-band .or { font-weight: 400; font-style: italic; }
  .brand {
    position: absolute; left: 0; right: 0; top: 880px;
    font-weight: 800; font-size: 56px; line-height: 1; color: var(--brand-green);
    text-transform: uppercase; letter-spacing: 1px;
  }
</style>
</head>
<body>
<main class="coaster">
  <h1 class="headline">
    <span class="headline__top">Zenith Wager</span>
    <span class="headline__bottom">Analytics!</span>
  </h1>

  <section class="features">
    <div class="feature">
      <svg class="feature__icon" viewBox="0 0 100 100" aria-hidden="true">
        <circle cx="50" cy="50" r="47" fill="var(--green)" stroke="var(--ink)" stroke-width="2.5"/>
        <g fill="none" stroke="var(--ink)" stroke-width="2" stroke-linejoin="round">
          <rect x="20" y="44" width="50" height="18" rx="1"/>
          <ellipse cx="45" cy="53" rx="7" ry="5"/>
          <path d="M20 66 h50 M20 70 h50 M20 74 h50"/>
          <circle cx="60" cy="30" r="9" fill="var(--green)"/>
          <circle cx="72" cy="38" r="9" fill="var(--green)"/>
        </g>
        <g font-family="Roboto Condensed, sans-serif" font-weight="700" font-size="11" fill="var(--ink)" text-anchor="middle">
          <text x="60" y="34">$</text><text x="72" y="42">$</text>
        </g>
      </svg>
      <p class="feature__label">Winnng<em>Results</em></p>
    </div>

    <div class="feature">
      <svg class="feature__icon" viewBox="0 0 100 100" aria-hidden="true">
        <circle cx="50" cy="50" r="47" fill="var(--green)" stroke="var(--ink)" stroke-width="2.5"/>
        <g fill="none" stroke="var(--ink)" stroke-width="2" stroke-linejoin="round">
          <path d="M24 20 V76 H80"/>
          <path d="M21 24 h3 M21 34 h3 M21 44 h3 M21 54 h3 M21 64 h3"/>
          <rect x="30" y="52" width="8" height="24"/>
          <rect x="42" y="58" width="8" height="18"/>
          <rect x="54" y="46" width="8" height="30"/>
          <rect x="66" y="30" width="8" height="46"/>
          <path d="M42 64 l8 -6 M42 70 l8 -6 M66 36 l8 -6 M66 44 l8 -6 M66 52 l8 -6 M66 60 l8 -6 M66 68 l8 -6"/>
        </g>
      </svg>
      <p class="feature__label">Dynamic<em>Spreadsheet</em></p>
    </div>

    <div class="feature">
      <svg class="feature__icon" viewBox="0 0 100 100" aria-hidden="true">
        <circle cx="50" cy="50" r="47" fill="var(--green)" stroke="var(--ink)" stroke-width="2.5"/>
        <g fill="none" stroke="var(--ink)">
          <circle cx="39" cy="58" r="15" stroke-width="6" stroke-dasharray="5.9 5.9"/>
          <circle cx="39" cy="58" r="12" stroke-width="2"/>
          <circle cx="39" cy="58" r="5" stroke-width="2"/>
          <circle cx="64" cy="34" r="10" stroke-width="5" stroke-dasharray="4.5 3.35"/>
          <circle cx="64" cy="34" r="7.5" stroke-width="2"/>
          <circle cx="64" cy="34" r="3" stroke-width="2"/>
        </g>
      </svg>
      <p class="feature__label">Comprehensive<em>Tools</em></p>
    </div>
  </section>

  <h2 class="prompt">CURIOUS?</h2>

  <section class="contact-band">
    <p>www.zenithwageranalytics.example <span class="or">or</span></p>
    <p>twitter.com/zenithforecast</p>
  </section>

  <p class="brand">Zenith Wager Analytics</p>
</main>
</body>
</html>
```